Brindle Barks Chews Pouch Design

I want a pouch design for my yak cheese dog chews. My competitor is golden tail, see attached. I want something minimalist like that where you see that there is only 3 ingredients, Yak milk, lime juice, Himalayan salt. I want it to say 100% natural 100% organic on it. Also odor free. There has to be a big see through window on it so you can see the products inside. Here is my logo and my competitor package. The package is 13cm x 17cm x 5cm. I have 5 sizes of bags to create but same image design

Target Market(s)

Pet owners

Industry/Entity Type

Dog products

Requirements
Must have
• « SMALL » « MIN NET WT 200 g / 5 PCS » and its important the 3 ingredients mentioned and 100% natural and organic must be very visible however the window must be big
Should not have
• The ingredients in the back

```html
<!DOCTYPE html>
<html lang="en">
<head>
<meta charset="utf-8">
<title>Brindle Barks Chews Pouch Design</title>
<link href="https://fonts.googleapis.com/css2?family=Luckiest+Guy&family=Amatic+SC:wght@700&family=Outfit:wght@400;600;700&family=Barlow+Condensed:wght@600;700&display=swap" rel="stylesheet">
<style>
:root{
  --tan:#e2bc69;
  --gusset:#c09236;
  --cream:#f8fad8;
  --orange:#f8a61f;
  --rust:#dc6a27;
  --brown:#b36a3c;
  --guide:#5a5a5a;
  --slate:#55565a;
  --silver:#b4b4b6;
}
*{margin:0;padding:0;box-sizing:border-box}
html,body{width:1200px;height:1016px;overflow:hidden;background:#fff}
.sheet{position:relative;width:1200px;height:1016px;background:#fff;font-family:"Outfit",sans-serif}
.abs{position:absolute}
.guide-v{position:absolute;top:0;width:1px;height:1016px;background:var(--guide);opacity:.6}
.guide-h{position:absolute;left:0;height:1px;width:1200px;background:var(--guide);opacity:.6}
.dash-h{position:absolute;height:0;border-top:1px dashed var(--guide);opacity:.7}
.fold-v{position:absolute;left:599px;top:0;height:1016px;border-left:2px dashed #4a4a4a}
.fold-h{position:absolute;left:23px;top:774px;width:577px;border-top:2px dashed #4a4a4a}

.front{left:23px;top:20px;width:577px;height:754px;background:var(--tan)}
.gusset{left:23px;top:774px;width:577px;height:222px;background:var(--gusset)}
.back{left:600px;top:20px;width:577px;height:722px;background:var(--tan)}

.odor{left:23px;top:35px;width:101px;height:172px;background:var(--orange)}
.odor span{position:absolute;left:50%;top:50%;transform:translate(-50%,-50%) rotate(90deg);font-family:"Amatic SC",sans-serif;font-size:46px;color:var(--cream);white-space:nowrap;letter-spacing:1px}

.claim{display:flex;align-items:center;justify-content:center;font-family:"Luckiest Guy",sans-serif;letter-spacing:2px}
.claim-natural{left:190px;top:32px;width:410px;height:63px;background:var(--cream);color:var(--brown);font-size:42px;padding-top:6px}
.claim-organic{left:193px;top:95px;width:407px;height:63px;background:var(--rust);color:var(--cream);font-size:40px;padding-top:6px}
.claim-size{left:420px;top:158px;width:180px;height:49px;background:var(--orange);color:var(--rust);font-size:32px;padding-top:5px}

.window{left:23px;top:199px;width:577px;height:281px;background:linear-gradient(160deg,#a9a9ab 0%,#d8d8d9 40%,#f3f3f3 75%,#fafafa 100%)}

.ingredients{left:311px;top:449px;width:289px;height:247px;background:var(--orange);text-align:center}
.ingredients .count{font-family:"Luckiest Guy",sans-serif;color:var(--rust);font-size:22px;letter-spacing:3px;margin-top:10px;padding-left:40px}
.ingredients .item{font-family:"Amatic SC",sans-serif;color:var(--cream);line-height:.95;padding-left:20px}
.i1{font-size:76px}.i2{font-size:54px}.i3{font-size:76px}

.weight{left:23px;top:685px;width:577px;height:80px;background:var(--rust)}
.weight span{position:absolute;left:90px;top:22px;font-family:"Luckiest Guy",sans-serif;font-size:35px;color:var(--cream);letter-spacing:2px}

.mascot{left:85px;top:450px;width:225px;height:225px;border-radius:50%;background:radial-gradient(circle at 50% 40%,#f0a840 0%,#c8782a 45%,#2f7f8c 75%,#2a5f3a 100%)}
.brand-name{left:70px;top:640px;width:250px;text-align:center;font-family:"Luckiest Guy",sans-serif;font-size:30px;color:#3a1a1e;line-height:1}

.about{left:616px;top:109px;width:547px;height:133px;background:var(--cream);text-align:center;padding:22px 30px 0;color:var(--rust)}
.about h3,.qui h3{font-size:15px;font-weight:700;margin-bottom:1px}
.about p,.qui p{font-size:12.3px;line-height:1.35}
.qui{left:616px;top:239px;width:547px;height:135px;background:var(--rust);text-align:center;padding:19px 30px 0;color:var(--cream)}
.qui p{text-align:justify;text-align-last:center}

.cautions{left:630px;top:371px;width:236px;height:238px;background:var(--orange);border-radius:0 0 18px 18px;color:var(--cream);padding:10px 14px 0 15px}
.cautions h4{text-align:center;font-size:15px;font-weight:700;margin:0 0 2px}
.cautions ul{list-style:none;font-size:9.6px;line-height:16px}
.cautions ul li::before{content:"• "}
.cautions h4.fr{margin-top:3px}

.nutrition{left:883px;top:384px;width:268px;height:223px;border:3px solid var(--cream);color:var(--cream)}
.nutrition h4{font-size:15px;font-weight:700;padding:6px 8px 4px;border-bottom:2px solid var(--cream)}
.nutrition table{width:100%;border-collapse:collapse}
.nutrition td{font-size:10.5px;font-weight:600;padding:0 3px 0 8px;border-bottom:1px solid var(--cream);height:27px}
.nutrition td.v{text-align:right}
.nutrition tr.head td{font-size:7.5px;line-height:1.1;height:28px}
.nutrition tr:last-child td{border-bottom:none}

.recipe{left:626px;top:622px;width:523px;height:109px;background:var(--cream);border:3px solid var(--rust);border-radius:14px}
.recipe h4{position:absolute;left:0;right:0;top:4px;text-align:center;font-family:"Luckiest Guy",sans-serif;font-size:19px;color:var(--rust);letter-spacing:1.5px}
.step{position:absolute;top:27px;display:flex;gap:5px;color:var(--rust)}
.step b{font-family:"Luckiest Guy",sans-serif;font-size:15px;font-weight:400}
.step p{font-size:9.5px;font-style:italic;font-weight:600;line-height:1.35}
.recipe svg{position:absolute}

.logo-mark{left:670px;top:805px;width:150px;height:150px;border-radius:50%;background:var(--rust)}
.logo-name{left:670px;top:955px;width:150px;text-align:center;font-family:"Luckiest Guy",sans-serif;font-size:15px;color:var(--rust)}
.title{left:826px;top:852px;font-family:"Barlow Condensed",sans-serif;font-weight:700;line-height:1}
.title .t1{font-size:38px;color:var(--slate);letter-spacing:.5px}
.title .t2{font-size:34px;color:var(--silver);margin-left:40px;margin-top:2px;letter-spacing:.5px}
</style>
</head>
<body>
<div class="sheet">
  <!-- panels -->
  <div class="abs front"></div>
  <div class="abs gusset"></div>
  <div class="abs back"></div>

  <!-- front -->
  <div class="abs odor"><span>ODOR FREE</span></div>
  <div class="abs claim claim-natural">100% NATURAL</div>
  <div class="abs claim claim-organic">100%ORGANIC</div>
  <div class="abs claim claim-size">SMALL</div>
  <div class="abs window" role="img" aria-label="Clear see-through window showing the chews inside"></div>

  <div class="abs ingredients">
    <div class="count">3 INGREDIENTS</div>
    <div class="item i1">YALK MILK</div>
    <div class="item i2">HIMALAYAN SALT</div>
    <div class="item i3">LIME JUICE</div>
  </div>
  <div class="abs weight"><span>MIN NET WT 200G / 5PCS</span></div>

  <div class="abs mascot" role="img" aria-label="Brand mascot illustration with mountain scenery"></div>
  <div class="abs brand-name">BRINDLE BARKS CHEWS</div>

  <!-- back -->
  <div class="abs about">
    <h3>About us:</h3>
    <p>At Brindle Barks Chews, we believe that dogs deserve the best. That’s why our chews are made with 100% natural, organic ingredients, ensuring your dog enjoys a healthy, delicious treat. With a focus on quality, we aim to provide a product that reflects our love for dogs and our dedication to their health and happiness.</p>
  </div>
  <div class="abs qui">
    <h3>Qui sommes-nous:</h3>
    <p>Chez Brindle Barks Chews, nous croyons que les chiens méritent le meilleur, Meilleur, c’est pourquoi nos gâteries sont fabriquées à partir d’ingrédients 100% naturels et biologiques, garantissant un régal sain et délicieux pour votre chien. Nous visons à offrir un produit de qualité qui reflète notre amour pour les chiens et notre dévouement envers leur santé et leur bonheur.</p>
  </div>

  <div class="abs cautions">
    <h4>Cautions:</h4>
    <ul>
      <li>Not for human consummption</li>
      <li>Supervies pets while giving any treats.</li>
      <li>Wash hands after handling.</li>
      <li>Remove treat if product breaks into sharp pieces.</li>
    </ul>
    <h4 class="fr">Mises en garde:</h4>
    <ul>
      <li>Pour consommation animale seulement</li>
      <li>Surveillez vos amis poilus lorsqu’ils grugent des gâteries.</li>
      <li>Lavez-vous les mains après manipulation.</li>
      <li>Retirez la gâterie si le produit se casse en morceaux pointus.</li>
    </ul>
  </div>

  <div class="abs nutrition">
    <h4>Nutrition Facts/Valeur Nutritive</h4>
    <table>
      <tr class="head"><td>Amount<br>Teneur</td><td class="v">%Daily Amount<br>%Valeur quotidienne</td></tr>
      <tr><td>Energy Level</td><td class="v">355 KCAL/100G</td></tr>
      <tr><td>Crude Protein</td><td class="v">65%Min</td></tr>
      <tr><td>Crude Fat</td><td class="v">1%Min</td></tr>
      <tr><td>Carbohydrates</td><td class="v">10%</td></tr>
      <tr><td>Ashes</td><td class="v">10% Max</td></tr>
      <tr><td>Moisture</td><td class="v">10% Max</td></tr>
    </table>
  </div>

  <div class="abs recipe">
    <h4>CRUNCHY PUFF RECIPE</h4>
    <div class="step" style="left:14px"><b>1.</b><p>Remove the Chewed<br>down end piece</p></div>
    <div class="step" style="left:136px"><b>2.</b><p>Soak in warm water<br>for 5 minutes.</p></div>
    <div class="step" style="left:255px"><b>3.</b><p>Microwave for 30<br>seconds.</p></div>
    <div class="step" style="left:366px"><b>4.</b><p>Let it cool for 2 minutes,<br>then serve to your dog as<br>a crunchy treat!</p></div>
    <svg style="left:52px;top:63px" width="32" height="32" viewBox="0 0 32 32" fill="none" stroke="#dc6a27" stroke-width="1.6"><path d="M6 10 16 5 26 10 26 22 16 27 6 22Z"/><path d="M6 10 16 15 26 10M16 15V27"/></svg>
    <svg style="left:164px;top:62px" width="70" height="36" viewBox="0 0 70 36"><path d="M2 3H68Q66 33 35 34Q4 33 2 3Z" fill="#dc6a27"/><path d="M27 14 35 10 43 14 43 24 35 28 27 24Z" fill="none" stroke="#f8fad8" stroke-width="1.5"/></svg>
    <svg style="left:286px;top:58px" width="58" height="40" viewBox="0 0 58 40" fill="none" stroke="#dc6a27" stroke-width="1.6"><rect x="1" y="1" width="56" height="38" rx="2"/><rect x="5" y="5" width="38" height="30"/><path d="M47 8h6M47 13h6M47 18h6"/><path d="M18 16 24 13 30 16 30 24 24 27 18 24Z"/></svg>
    <svg style="left:429px;top:56px" width="28" height="40" viewBox="0 0 28 40" fill="none" stroke="#dc6a27" stroke-width="1.6"><path d="M9 2q-3 4 0 8M14 2q-3 4 0 8M19 2q-3 4 0 8"/><path d="M4 18 14 13 24 18 24 31 14 36 4 31Z"/><path d="M4 18 14 23 24 18M14 23V36"/></svg>
  </div>

  <!-- presentation label -->
  <div class="abs logo-mark" role="img" aria-label="Brand mascot illustration"></div>
  <div class="abs logo-name">BRINDLE BARKS</div>
  <div class="abs title"><div class="t1">BRINDLE BARKS CHEWS</div><div class="t2">POUCH DESIGN</div></div>

  <!-- print guides -->
  <div class="guide-v" style="left:23px"></div>
  <div class="guide-v" style="left:52px"></div>
  <div class="guide-v" style="left:569px"></div>
  <div class="guide-v" style="left:631px"></div>
  <div class="guide-v" style="left:1145px"></div>
  <div class="guide-v" style="left:1177px"></div>
  <div class="guide-h" style="top:20px"></div>
  <div class="guide-h" style="top:742px"></div>
  <div class="guide-h" style="top:774px"></div>
  <div class="guide-h" style="top:996px"></div>
  <div class="dash-h" style="left:0;top:99px;width:1200px"></div>
  <div class="dash-h" style="left:0;top:126px;width:1200px"></div>
  <div class="dash-h" style="left:0;top:157px;width:1200px"></div>
  <div class="fold-v"></div>
  <div class="fold-h"></div>
</div>
</body>
</html>
```